Wine label

I'm wanting to create a wine label that is very very simple, but eye catching. Jump off the shelf.

Name of Winery : Marlow Ridge

Nothing on the front but that - will be putting other info on back - which will be the brand label.

I was thinking of something MR - possibly - with marlow ridge intertwined. -

1 color label and possible 1 or 2 ink

```html
<!DOCTYPE html>
<html lang="en">
<head>
<meta charset="utf-8">
<title>Marlow Ridge — Wine Label</title>
<link rel="stylesheet" href="https://fonts.googleapis.com/css2?family=Barlow:wght@500&family=Montserrat:wght@900&display=swap">
<style>
  :root {
    --backdrop: #7b7b7b;
    --label-ground: #1f1f20;
    --seal-fill: #3c3c3d;
    --name-ink: #d6d6d7;
    --initial-grey: #c9cacc;
    --initial-teal: #3dbfab;
  }
  * { box-sizing: border-box; margin: 0; padding: 0; }
  html, body {
    width: 963px;
    height: 1200px;
    overflow: hidden;
    background: var(--backdrop);
  }
  .canvas {
    position: relative;
    width: 963px;
    height: 1200px;
  }
  .wine-label {
    position: absolute;
    left: 271px;
    top: 117px;
    width: 420px;
    height: 966px;
    background: var(--label-ground);
    overflow: hidden;
  }
  .monogram {
    position: absolute;
    inset: 0;
    width: 420px;
    height: 966px;
  }
  .monogram text {
    font-family: "Montserrat", "Arial Black", sans-serif;
    font-weight: 900;
    font-size: 360px;
  }
  .initial-upper { fill: var(--initial-grey); }
  .initial-lower { fill: var(--initial-teal); }
  .brand-seal {
    position: absolute;
    left: 38px;
    top: 25px;
    width: 382px;
    height: 382px;
    border-radius: 50%;
    background: var(--seal-fill);
  }
  .brand-name {
    position: absolute;
    left: 132px;
    top: 160px;
    font-family: "Barlow", "DIN Alternate", sans-serif;
    font-weight: 500;
    font-size: 44px;
    line-height: 1;
    letter-spacing: 2px;
    color: var(--name-ink);
    text-transform: uppercase;
  }
  .brand-name span { display: block; }
</style>
</head>
<body>
  <main class="canvas">
    <section class="wine-label" aria-label="Marlow Ridge wine label">
      <svg class="monogram" viewBox="0 0 420 966" aria-hidden="true">
        <text class="initial-upper" x="24" y="610" textLength="374" lengthAdjust="spacingAndGlyphs">M</text>
        <text class="initial-lower" x="24" y="952" textLength="374" lengthAdjust="spacingAndGlyphs">R</text>
      </svg>
      <div class="brand-seal" aria-hidden="true"></div>
      <h1 class="brand-name"><span>Marlow</span><span>Ridge</span></h1>
    </section>
  </main>
</body>
</html>
```